Book cover for book of Poems "Lanternfall"

I have written a book of poems. The book is titled "Lanternfall" and has 160 pages. The poems were written mostly during my youth but there are newer poems also written over the past 10 years (I'm 42 now). They are mostly about love, loss, social conformity, and nature. I'm influenced a lot by the English Romantic Poets, gothic motives, and 80s music by bands such as The Vell, Porvana & the Quillets, and Tabberley. I need an original book cover design for my book. Attached are samples of designs I like and few of my poems. The cover will be a hardcover and I need design for Front Cover, Back Cover, and Spine. Dimension is 6"x9". Front Cover should have name of book "Lanternfall" and name of author "Ravi Dunsker". Thanks.
Updates

Further details which I should have included in my original brief -The book cover will be a hard cover. Design is required for front cover, back cover, and spine. Dimension is 6x9.Front should have book title "Lanternfall" and author's name "Ravi Dunsker". Added Monday, December 19, 2016

Target Market(s)

Mostly friends and family

Requirements
Must have
• I don't mind a design where lanternfall is spelled out in big capital letters and text from one of my poems is inside, like the sample I've attached.

```html
<!DOCTYPE html>
<html lang="en">
<head>
<meta charset="utf-8">
<title>Lanternfall — Book Cover Wrap</title>
<link rel="stylesheet" href="https://fonts.googleapis.com/css2?family=Cormorant+Garamond:ital,wght@0,400;0,500;1,400;1,500&family=Allura&display=swap">
<style>
  :root {
    --backdrop: #e4e0dc;
    --cover-deep: #050505;
    --cover-lift: #3b3b3d;
    --spine-deep: #0c0c0c;
    --spine-sheen: #4a4a4c;
    --ink-white: #f1f1f1;
    --title-slate: #6e7788;
    --verse-faint: #3a3d43;
    --verse-bright: #b9bcc2;
    --placeholder-grey: #c4c4c4;
    --imprint-gold: #c9a24a;
  }
  * { margin: 0; padding: 0; box-sizing: border-box; }
  html, body {
    width: 1200px; height: 800px; overflow: hidden;
    background: var(--backdrop);
  }
  .wrap {
    position: absolute; left: 132px; top: 70px;
    width: 936px; height: 660px;
    display: flex;
    box-shadow: 0 18px 40px rgba(0,0,0,0.25);
  }
  .back-cover, .front-cover {
    position: relative; width: 440px; height: 660px;
  }
  .back-cover {
    background: linear-gradient(135deg, var(--cover-deep) 0%, #141414 55%, #262627 100%);
  }
  .front-cover {
    background: linear-gradient(150deg, var(--cover-deep) 0%, #151516 45%, var(--cover-lift) 100%);
    overflow: hidden;
  }
  .spine {
    position: relative; width: 56px; height: 660px;
    background: linear-gradient(90deg, var(--spine-deep) 0%, #222 40%, var(--spine-sheen) 70%, #1a1a1a 100%);
  }
  .spine-text {
    position: absolute; left: 50%; top: 28px;
    transform-origin: 0 0;
    transform: rotate(90deg) translateY(-50%);
    display: flex; align-items: center; gap: 70px;
    white-space: nowrap;
  }
  .spine-author {
    font-family: "Cormorant Garamond", serif;
    font-size: 15px; letter-spacing: 4px; line-height: 18px;
    color: var(--ink-white); text-transform: uppercase;
  }
  .spine-title {
    font-family: "Cormorant Garamond", serif; font-style: italic;
    font-size: 34px; color: var(--title-slate);
  }
  .imprint {
    position: absolute;
    width: 36px; height: 36px;
    border: 1px solid var(--imprint-gold);
    display: flex; align-items: center; justify-content: center; text-align: center;
    font-family: "Cormorant Garamond", serif;
    font-size: 5px; letter-spacing: 0.5px; line-height: 6px;
    color: var(--ink-white); text-transform: uppercase;
  }
  .spine .imprint { left: 10px; bottom: 30px; }
  .back-cover .imprint { left: 34px; bottom: 34px; }
  .back-placeholder {
    position: absolute; left: 36px; bottom: 150px;
    width: 118px; height: 118px;
    background: var(--placeholder-grey);
  }
  .front-author {
    position: absolute; top: 34px; left: 0; right: 0; text-align: center;
    font-family: "Cormorant Garamond", serif;
    font-size: 16px; letter-spacing: 5px;
    color: var(--ink-white); text-transform: uppercase;
  }
  .verse {
    position: absolute; left: 0; right: 0; text-align: center;
    font-family: "Allura", cursive;
    font-size: 19px; line-height: 27px;
  }
  .verse-upper { top: 150px; }
  .verse-lower { top: 520px; }
  .verse .faint { color: var(--verse-faint); }
  .verse .bright { color: var(--verse-bright); }
  .stanza-gap { height: 14px; }
  .front-title {
    position: absolute; left: 40px; top: 430px;
    font-family: "Cormorant Garamond", serif; font-style: italic; font-weight: 500;
    font-size: 78px; color: var(--title-slate);
  }
</style>
</head>
<body>
  <main class="wrap">
    <section class="back-cover" aria-label="Back cover">
      <div class="back-placeholder" aria-hidden="true"></div>
      <div class="imprint">Logo Placeholder</div>
    </section>

    <section class="spine" aria-label="Spine">
      <div class="spine-text">
        <span class="spine-author">Ravi<br>Dunsker</span>
        <span class="spine-title">Lanternfall</span>
      </div>
      <div class="imprint">Logo Placeholder</div>
    </section>

    <section class="front-cover" aria-label="Front cover">
      <p class="front-author">Ravi Dunsker</p>
      <div class="verse verse-upper">
        <p class="faint">The lamps went dark along the shore</p>
        <p class="faint">And we forgot the way back home</p>
        <p class="faint">The lamps went dark along the shore</p>
        <p class="faint">Our names were lost in falling foam</p>
        <div class="stanza-gap"></div>
        <p class="bright">Where did the light go</p>
        <p class="bright">Who let the candle drown</p>
        <p class="faint">We held the flame so close</p>
        <p class="faint">And watched it tumble down</p>
      </div>
      <h1 class="front-title">Lanternfall</h1>
      <div class="verse verse-lower">
        <p class="faint">Each lantern falls into the tide</p>
        <p class="faint">And carries what we could not say</p>
        <p class="faint">The night remembers all we hid</p>
      </div>
    </section>
  </main>
</body>
</html>
```